Vehicle Artwork to look like emergency response plumber

We need artwork designed for our company fleet, we would like to start with our truck. We would like the vehicle to stand out as an Emergency Response Vehicle (We would like this detailed on the vehicle as well). I have uploaded two different artworks that have been designed by signwriters, however, it looks too busy with not a lot of information. We do all scopes of plumbing and gas works, specialising in Emergency Works. The following could also be listed on the vehicle:
Leak Detection
Burst Pipes
Blocked Drains
Gas Leaks
All Major and Minor Plumbing Works
Industrial, Commercial, Marine, Mining & Domestic
LOGO on Doors must be striped or patterned

Target Market(s)

emergency plumbing works

Industry/Entity Type

Plumbing and gas

Font styles to use
Serif

Colors
EB3D1F
EC4F4E
F09395
F8D3D4
FCEDEE

Requirements
Must have
• company logo rk4619 (in very small font) phone number, emergency response vehicle
Nice to have
• pattern

```html
<!DOCTYPE html>
<html lang="en">
<head>
<meta charset="utf-8">
<title>Emergency Plumbing Perth – Truck Side Panel</title>
<link href="https://fonts.googleapis.com/css2?family=Montserrat:ital,wght@0,400;0,600;0,700;0,800;1,800&display=swap" rel="stylesheet">
<style>
  :root {
    --stage: #2a2a2a;
    --panel-face: #ececec;
    --panel-rail: #d9d9d9;
    --panel-edge: #c4c4c4;
    --red: #e8333f;
    --red-light: #f0566a;
    --red-deep: #c9303d;
    --ink: #2b2b2b;
    --white: #ffffff;
    --inset: #e4e4e4;
  }
  * { margin: 0; padding: 0; box-sizing: border-box; }
  html, body { width: 1200px; height: 857px; overflow: hidden; background: var(--stage); }
  body { position: relative; font-family: "Montserrat", sans-serif; }

  .box-side {
    position: absolute;
    left: 30px; top: 148px;
    width: 1170px; height: 575px;
    transform: scale(0.974);
    transform-origin: top left;
  }
  .box-side__shapes { position: absolute; inset: 0; }

  .sectors {
    position: absolute; left: 60px; top: 45px;
    font-size: 21px; font-weight: 800; letter-spacing: 0.6px;
    color: var(--red);
  }
  .brand-mark {
    position: absolute; left: 112px; top: 205px;
    width: 66px; height: 66px; background: var(--red);
  }
  .divider {
    position: absolute; left: 214px; top: 155px;
    width: 2px; height: 185px; background: var(--ink);
  }
  .headline {
    position: absolute; left: 245px; top: 188px;
    font-size: 38px; font-weight: 600; line-height: 40px; letter-spacing: 3.5px;
  }
  .headline__line--red { color: var(--red); }
  .headline__line--dark { color: var(--ink); }

  .services {
    position: absolute; left: 548px; top: 184px;
    list-style: none;
    font-size: 21px; font-weight: 400; line-height: 36px; color: var(--ink);
  }
  .services li { position: relative; padding-left: 17px; }
  .services li::before {
    content: ""; position: absolute; left: 0; top: 18px;
    width: 7px; height: 3px; background: var(--red);
  }
  .services li.services__cont::before { display: none; }

  .phone {
    position: absolute; left: 418px; top: 468px;
    font-size: 37px; font-weight: 800; font-style: italic; letter-spacing: 2px;
    color: var(--white);
  }
  .company-name {
    position: absolute; left: 788px; top: 472px;
    width: 160px;
    text-align: center;
    font-size: 13px; font-weight: 700; line-height: 16px; letter-spacing: 0.5px;
    color: var(--white);
  }
  .company-name__main { display: block; font-size: 13px; letter-spacing: 3px; }
</style>
</head>
<body>
  <section class="box-side">
    <svg class="box-side__shapes" viewBox="0 0 1170 575" width="1170" height="575" aria-hidden="true">
      <defs>
        <linearGradient id="bandGradient" x1="0" y1="0" x2="1" y2="0">
          <stop offset="0" stop-color="#f26a7c"/>
          <stop offset="0.5" stop-color="#e8414f"/>
          <stop offset="1" stop-color="#d8303e"/>
        </linearGradient>
      </defs>
      <rect x="0" y="0" width="1170" height="575" fill="var(--panel-face)"/>
      <rect x="0" y="0" width="1170" height="30" fill="var(--panel-rail)"/>
      <line x1="0" y1="30" x2="1170" y2="30" stroke="var(--panel-edge)" stroke-width="2"/>
      <rect x="0" y="545" width="1170" height="30" fill="var(--panel-rail)"/>
      <line x1="0" y1="545" x2="1170" y2="545" stroke="var(--panel-edge)" stroke-width="2"/>
      <rect x="1132" y="0" width="38" height="575" fill="#f4f4f4"/>
      <line x1="1132" y1="0" x2="1132" y2="575" stroke="var(--panel-edge)" stroke-width="2"/>
      <polygon points="880,33 1065,33 1065,98 842,98" fill="url(#bandGradient)"/>
      <rect x="842" y="99" width="290" height="326" fill="var(--inset)" stroke="#9a9a9a" stroke-width="1"/>
      <path d="M395 424 L1132 422 L1132 428 L388 430 Z" fill="var(--ink)"/>
      <path d="M385 432 Q700 420 1132 430 L1132 543 L250 543 Z" fill="url(#bandGradient)"/>
      <circle cx="990" cy="490" r="17" fill="var(--white)" opacity="0.92"/>
      <circle cx="1043" cy="490" r="17" fill="var(--white)" opacity="0.92"/>
      <circle cx="1096" cy="490" r="17" fill="var(--white)" opacity="0.92"/>
    </svg>

    <p class="sectors">INDUSTRIAL, COMMERCIAL, MARINE, MINING &amp; DOMESTIC</p>

    <div class="brand-mark"></div>
    <div class="divider"></div>
    <h1 class="headline">
      <span class="headline__line--red">EMERGENCY</span><br>
      <span class="headline__line--dark">PLUMBING</span><br>
      <span class="headline__line--red">PERTH</span>
    </h1>

    <ul class="services">
      <li>LEAK DETECTION</li>
      <li>BURST PIPES</li>
      <li>BLOCKED DRAINS</li>
      <li>GAS LEAKS</li>
      <li>ALL MAJOR AND MINOR</li>
      <li class="services__cont">PLUMBING WORKS</li>
    </ul>

    <p class="phone">08 5550 0147</p>
    <p class="company-name"><span class="company-name__main">RK4619</span>PLUMBING &amp; GAS</p>
  </section>
</body>
</html>
```